Mistholm Consulting Business

** Please add the content information from my old business card
1. I would like to see a two sided business card with both options with the 1st Option--Sketch Forge-new WHITE BACKGROUND LOGO
2 nd Option-Sketch Forge - new BLACK- Background Logo
3rd -Option a business card with my Photo on the card
Please add the new word to the card information:
EXECUTION
AS THE OWNER'S REP
WE AIM TO ACHIEVE YOUR
INFRASTRUCTURE VISION with
OUR SPECIALIZATION & EXECUTION in:

FUNDING Planning
BUSINESS Planning
INFRASTRUCTURE Planning
PROJECT Management
Since 2012
_____________________________________________________________________
I want to get spot uv raised printing. I was liking a a nice rich white linen paper stock with black writing & NOT A COLORED CARD other than a variety of white or black cards concept

```html
<!DOCTYPE html>
<html lang="en">
<head>
<meta charset="UTF-8">
<title>Mistholm Consulting – Business Card</title>
<link href="https://fonts.googleapis.com/css2?family=Open+Sans:wght@400;600;700&display=swap" rel="stylesheet">
<style>
  :root {
    --stage: #232323;
    --card: #1b1b1d;
    --card-edge: #121213;
    --ink: #ffffff;
    --ink-soft: #d9d9d9;
    --accent: #e0161d;
    --photo-top: #2c2b2c;
    --photo-mid: #4a3a30;
    --photo-dark: #0f0f10;
    --leaf-light: #3a3a3c;
    --leaf-dark: #0b0b0c;
  }
  * { box-sizing: border-box; margin: 0; padding: 0; }
  html, body {
    width: 1200px; height: 780px; overflow: hidden;
    background: var(--stage);
    font-family: "Open Sans", Arial, sans-serif;
    color: var(--ink);
  }
  .stage { position: relative; width: 1200px; height: 780px; }
  .card {
    position: absolute; top: 240px;
    width: 525px; height: 300px;
    background: var(--card);
    border-radius: 4px;
    overflow: hidden;
    box-shadow: 0 4px 0 var(--card-edge), 0 8px 0 var(--card-edge), 0 24px 40px rgba(0,0,0,.55);
  }
  .card--front { left: 50px; }
  .card--back { left: 625px; }

  /* Front */
  .brand-name {
    position: absolute; left: 34px; top: 30px;
    font-weight: 700; font-size: 26px; letter-spacing: .5px;
    display: flex; align-items: center; gap: 10px;
  }
  .brand-dot { width: 10px; height: 10px; background: var(--accent); }
  .holder {
    position: absolute; left: 26px; top: 84px;
    border-left: 6px solid var(--accent); padding-left: 10px;
  }
  .holder-name { color: var(--accent); font-weight: 700; font-size: 20px; line-height: 1.15; white-space: nowrap; }
  .holder-title { font-size: 11.5px; letter-spacing: .4px; color: var(--ink-soft); margin-top: 4px; }
  .contact-list { position: absolute; left: 34px; top: 158px; list-style: none; }
  .contact-item { display: flex; align-items: center; gap: 8px; font-size: 13px; line-height: 22px; }
  .contact-icon { width: 13px; height: 13px; fill: var(--accent); }
  .offices { position: absolute; left: 34px; top: 234px; font-size: 13.5px; font-weight: 600; }
  .offices-dot { color: var(--accent); margin: 0 4px; }
  .portrait {
    position: absolute; right: 0; bottom: 0; width: 200px; height: 180px;
    background: linear-gradient(160deg, var(--photo-top) 0%, var(--photo-mid) 45%, var(--photo-dark) 100%);
  }

  /* Back */
  .leaf-mark {
    position: absolute; left: 20px; top: 14px; width: 240px; height: 230px;
    border-radius: 50% 50% 44% 44%;
    background: linear-gradient(135deg, var(--leaf-dark) 0%, var(--leaf-dark) 45%, var(--leaf-light) 100%);
  }
  .back-brand {
    position: absolute; left: 56px; top: 104px;
    font-weight: 700; font-size: 26px;
    display: flex; align-items: center; gap: 10px;
  }
  .pitch {
    position: absolute; right: 30px; top: 108px; text-align: right;
    font-size: 11.5px; letter-spacing: .6px; line-height: 17px;
  }
  .services { margin-top: 10px; font-size: 13px; line-height: 18px; }
  .service strong { font-weight: 700; }
  .service--accent { color: var(--accent); }
</style>
</head>
<body>
<main class="stage">
  <section class="card card--front" aria-label="Card front">
    <div class="brand-name"><span>Mistholm</span><span class="brand-dot"></span></div>
    <div class="holder">
      <p class="holder-name">Dana Whitcombe-Rivers</p>
      <p class="holder-title">CEO / LEAD PROJECT MANAGER</p>
    </div>
    <ul class="contact-list">
      <li class="contact-item">
        <svg class="contact-icon" viewBox="0 0 24 24"><path d="M6.6 10.8a15 15 0 0 0 6.6 6.6l2.2-2.2a1 1 0 0 1 1-.25 11.4 11.4 0 0 0 3.6.6 1 1 0 0 1 1 1V20a1 1 0 0 1-1 1A17 17 0 0 1 3 4a1 1 0 0 1 1-1h3.5a1 1 0 0 1 1 1c0 1.25.2 2.45.6 3.6a1 1 0 0 1-.25 1z"/></svg>
        867.555.0192
      </li>
      <li class="contact-item">
        <svg class="contact-icon" viewBox="0 0 24 24"><path d="M2 5h20v14H2z M2 5l10 8 10-8" fill="none" stroke="#e0161d" stroke-width="2.4"/></svg>
        dana@mistholm.ca
      </li>
      <li class="contact-item">
        <svg class="contact-icon" viewBox="0 0 24 24"><circle cx="12" cy="12" r="9" fill="none" stroke="#e0161d" stroke-width="2.4"/><path d="M3 12h18M12 3c3 3 3 15 0 18M12 3c-3 3-3 15 0 18" fill="none" stroke="#e0161d" stroke-width="1.8"/></svg>
        www.mistholm.ca
      </li>
    </ul>
    <p class="offices">Northgate NT<span class="offices-dot">●</span>Riverton NB</p>
    <div class="portrait" role="img" aria-label="Portrait photograph of the card holder against a dark backdrop"></div>
  </section>

  <section class="card card--back" aria-label="Card back">
    <div class="leaf-mark" role="img" aria-label="Large raised spot UV leaf decoration"></div>
    <div class="back-brand"><span>Mistholm</span><span class="brand-dot"></span></div>
    <div class="pitch">
      <p>AS THE OWNER'S REP</p>
      <p>WE AIM TO ACHIEVE YOUR</p>
      <p>INFRASTRUCTURE VISION with</p>
      <p>OUR SPECIALIZATION &amp; EXECUTION in:</p>
      <div class="services">
        <p class="service"><strong>FUNDING</strong> Planning</p>
        <p class="service service--accent"><strong>BUSINESS</strong> Planning</p>
        <p class="service"><strong>PROJECT</strong> Management</p>
        <p class="service service--accent"><strong>INFRASTRUCTURE</strong> Planning</p>
      </div>
    </div>
  </section>
</main>
</body>
</html>
```